Eco conscious print and frame company needs a website

‘LUMAeco is a new company that makes frames and fine art prints from sustainable bamboo. Our site should have an organic feel yet still have a professional clean look to it as well.
We need shopping cart and image uploading capabilities much like a pictorama or glowbird type of site only on a much smaller scale.
Currently we have 3 different styles available in sizes from 8"x8" all the way to 4ft by 8ft.
Target audience will be the snapvintra, pixelgram, zephone market.

Target Market(s)

20-40 years old male and female. Pixelgram generation.

Industry/Entity Type

Shopping

Requirements
Must have
• Front end and back end capabilities with emphasis on image uploading and shopping cart functionality.

```html
<!DOCTYPE html>
<html lang="en">
<head>
<meta charset="utf-8">
<title>LUMAeco Frame Company</title>
<link href="https://fonts.googleapis.com/css2?family=Ubuntu:ital,wght@0,400;0,500;0,700;1,700&family=Arimo:ital,wght@0,400;0,700;1,700&display=swap" rel="stylesheet">
<style>
:root{
  --green:#5aa71f;
  --green-dark:#2e7d1a;
  --green-deep:#1f6b16;
  --green-light:#8bd13a;
  --wood:#a25a2a;
  --wood-dark:#7c3f1a;
  --wood-light:#bf7439;
  --orange:#e0862a;
  --orange-dark:#b8601a;
  --olive:#4d4a2c;
  --card:#c49a66;
  --ink:#222;
  --white:#fff;
  --footer:#2f2f2f;
}
*{box-sizing:border-box;margin:0;padding:0}
html,body{width:960px;height:1200px;overflow:hidden}
body{position:relative;font-family:"Arimo",sans-serif;color:var(--ink);background:var(--white)}
.abs{position:absolute}

/* header */
.site-header{left:0;top:0;width:960px;height:124px;background:linear-gradient(#fff,#f1f1f1);border-bottom:1px solid #d8d8d8}
.brand{left:96px;top:60px;display:flex;align-items:center;gap:8px}
.brand-dot{width:18px;height:18px;border-radius:50%;background:var(--green)}
.brand-name{font-family:"Ubuntu",sans-serif;font-weight:500;font-size:26px;color:var(--green-dark)}
.field{top:16px;height:19px;border-radius:3px;background:linear-gradient(#d6d6d6,#bdbdbd);font-family:"Ubuntu",sans-serif;font-size:9px;color:#fff;padding:4px 18px;border:1px solid #c8c8c8}
.field.cat{left:480px;width:120px}
.field.cat::after{content:"";position:absolute;right:8px;top:8px;border:4px solid transparent;border-top-color:#fff}
.field.search{left:608px;width:159px}
.account{left:787px;top:18px;font-family:"Ubuntu",sans-serif;font-size:10px;color:#888}
.account .sep{margin:0 9px}
.main-nav{left:388px;top:92px;display:flex;height:32px;align-items:center;font-family:"Ubuntu",sans-serif;font-size:10.5px;font-weight:500;text-transform:uppercase}
.main-nav a{color:#222;text-decoration:none;margin-right:42px}
.main-nav a.current{background:linear-gradient(var(--green-light),var(--green));color:#fff;height:32px;line-height:36px;padding:0 18px;border-radius:7px 7px 0 0;margin-right:27px}

/* wood */
.wood{left:0;top:124px;width:960px;height:728px;
  background:
   repeating-linear-gradient(90deg,rgba(0,0,0,.22) 0 1px,transparent 1px 128px),
   repeating-linear-gradient(90deg,rgba(255,255,255,.05) 0 6px,rgba(0,0,0,.05) 6px 13px),
   linear-gradient(var(--wood-light),var(--wood) 50%,var(--wood-dark))}

/* hero */
.hero{left:81px;top:141px;width:798px;height:337px;background:linear-gradient(var(--green-light),var(--green));border:1px solid #a7d86a;box-shadow:0 14px 24px rgba(0,0,0,.35)}
.hero h1{left:28px;top:50px;font-family:"Ubuntu",sans-serif;font-weight:700;font-size:26px;color:#fff;text-shadow:0 1px 2px rgba(0,0,0,.25)}
.hero .lead{left:31px;top:94px;width:376px;font-family:"Ubuntu",sans-serif;font-weight:700;font-size:14.5px;line-height:19px;color:#fff;text-align:justify}
.hero .body{left:31px;top:173px;width:374px;font-size:9.6px;line-height:14.5px;color:#fff;text-align:justify}
.hero .body em{font-weight:700}
.btn{top:263px;width:122px;height:38px;border-radius:7px;background:linear-gradient(#eaa048,var(--orange-dark));border:2px solid #f7d08f;font-family:"Ubuntu",sans-serif;font-weight:500;font-size:12px;color:#fff;text-align:center;line-height:34px;white-space:nowrap}
.hero-photo{left:480px;top:22px;width:290px;height:290px;background:radial-gradient(circle at 50% 50%,#6b7a3c 0 30%,#e9c8a0 32% 55%,transparent 70%),linear-gradient(135deg,#f0d2ac,#cfa57a);transform:rotate(-6deg);border-radius:4px;box-shadow:0 8px 18px rgba(0,0,0,.3)}
.arrow{top:294px;width:35px;height:34px;background:rgba(70,40,20,.55);color:#d9b994;font-size:18px;text-align:center;line-height:34px}

/* offers */
.offer{top:537px;width:187px;height:148px;background:linear-gradient(#fff,#dedede);border:2px solid #fff;border-radius:7px;overflow:hidden;box-shadow:0 4px 10px rgba(0,0,0,.3)}
.offer-photo{right:0;top:26px;width:110px;height:120px;background:linear-gradient(135deg,#e9c8a0,#b98254)}
.offer-badge{left:6px;top:0;width:74px;height:76px;background:var(--green-deep);border-radius:0 0 0 30px;clip-path:polygon(0 0,100% 0,78% 100%,0 100%);padding:10px 0 0 7px;font-family:"Ubuntu",sans-serif;font-size:19px;line-height:18px;color:#fff}
.offer-cart{left:13px;bottom:0;width:24px;height:26px}

/* newsletter */
.newsletter{left:0;top:728px;width:955px;height:94px;background:var(--olive)}
.newsletter::before,.newsletter::after{content:"";position:absolute;left:0;right:0;border-top:2px dashed #cfc8a8}
.newsletter::before{top:3px}.newsletter::after{bottom:3px}
.badge{left:83px;top:725px;width:152px;height:108px;background:var(--white);transform:rotate(-5deg);box-shadow:0 3px 8px rgba(0,0,0,.4)}
.badge::after{content:"";position:absolute;inset:6px;background:var(--green-light)}
.parcel{left:232px;top:725px;width:257px;height:110px;background:linear-gradient(#d3ab77,var(--card));border-bottom:2px dashed #9c7a4d}
.parcel h2{left:26px;top:40px;font-family:"Ubuntu",sans-serif;font-weight:700;font-size:20px;color:#fff;text-shadow:0 2px 2px rgba(0,0,0,.35)}
.email{left:490px;top:757px;width:330px;height:38px;background:#fff;border:1px solid #ddd;font-family:"Ubuntu",sans-serif;font-size:15px;color:#aaa;padding:9px 20px}
.submit{left:810px;top:744px;width:64px;height:64px;border-radius:50%;background:radial-gradient(circle at 40% 35%,#ffa14a,#e0600f);border:2px solid #f2e6d3;font-family:"Ubuntu",sans-serif;font-weight:700;font-size:12px;color:#fff;text-align:center;line-height:60px;transform:rotate(-12deg)}

/* footer area */
.grass{left:0;top:852px;width:960px;height:308px;background:linear-gradient(#6fb727,var(--green) 40%,#4d9a18)}
.col-head{top:898px;width:184px;height:32px;background:linear-gradient(90deg,#4a4a32,#3a3a22 88%,transparent 88%);font-family:"Ubuntu",sans-serif;font-weight:700;font-size:12.5px;color:#fff;padding:8px 11px;white-space:nowrap}
.col-head::after{content:"";position:absolute;right:-8px;top:0;width:28px;height:32px;background:repeating-linear-gradient(135deg,transparent 0 6px,#a6e05b 6px 9px);clip-path:polygon(0 0,60% 50%,0 100%,40% 100%,100% 50%,40% 0)}
.blog{left:90px;top:946px;list-style:none;font-family:"Ubuntu",sans-serif;font-weight:500;font-size:8.8px;color:#fff}
.blog li{height:24px;padding-left:14px;position:relative}
.blog li::before{content:"";position:absolute;left:0;top:1px;width:4px;height:7px;border:solid #f3a83c;border-width:0 2px 2px 0;transform:rotate(40deg)}
.quote{left:283px;width:180px;font-family:"Ubuntu",sans-serif;font-size:8.8px;line-height:14.5px;color:#fff;padding-left:10px;white-space:nowrap}
.quote::before{content:"\201C";position:absolute;left:0;top:-2px;font-size:12px}
.quote a{display:block;margin-top:4px;font-weight:700;font-style:italic;font-size:9px;color:#fff;text-decoration:none}
.tweets{left:492px;width:170px;font-family:"Ubuntu",sans-serif;font-size:8.8px;line-height:14.5px;color:#fff;white-space:nowrap}
.tweets b{color:#1e1e1e}
.tweets span{color:#1e1e1e}
.tags{left:697px;top:944px;width:190px;font-family:"Ubuntu",sans-serif;font-size:10px;line-height:19.2px;color:#fff;white-space:nowrap}
.tags .big{font-size:17px}
.copyright{left:0;top:1160px;width:960px;height:40px;background:var(--footer);font-family:"Ubuntu",sans-serif;font-size:8.6px;color:#fff;text-align:center;line-height:48px}
</style>
</head>
<body>
<header class="site-header abs">
  <div class="brand abs"><span class="brand-dot"></span><span class="brand-name">LUMAeco</span></div>
  <div class="field cat abs">All Categories</div>
  <div class="field search abs">Search creative design</div>
  <div class="account abs">Sign Up<span class="sep">|</span>Log In</div>
  <nav class="main-nav abs">
    <a class="current" href="#">Home</a><a href="#">Custom Framing</a><a href="#">Services</a><a href="#">Gallery</a><a href="#">Contact &amp; Coupons</a>
  </nav>
</header>

<div class="wood abs"></div>

<section class="hero abs">
  <h1 class="abs">The Picture Frame Supermarket</h1>
  <p class="lead abs">We have over 600 custom frames and thousands of ready made frames to choose from. Join over 150,000 customers and choose LumaFRAME.</p>
  <p class="body abs"><em>Lorem Ipsum is simply dummy text of the printing and typesetting industry. Lorem Ipsum has been the industry's standard</em> dummy text ever since the 1500s, when an unknown printer took a galley of type and scrambled it to make a type specimen book. It has survived not only five centuries,</p>
  <div class="btn abs" style="left:35px">Frames By Size</div>
  <div class="btn abs" style="left:165px">Frames By Type</div>
  <div class="btn abs" style="left:296px">Frames By Colour</div>
  <div class="hero-photo abs" role="img" aria-label="Stacked bamboo picture frames holding a photo of a child on a tropical beach"></div>
</section>
<div class="arrow abs" style="left:73px">&#8249;</div>
<div class="arrow abs" style="left:851px">&#8250;</div>

<div class="offer abs" style="left:82px"><div class="offer-photo abs" role="img" aria-label="Corner of a bamboo frame with a metal wall fixing"></div><div class="offer-badge abs">Special<br>Offer<br>25%</div><svg class="offer-cart abs" viewBox="0 0 24 26"><path d="M0 8 12 0 24 8V26H0Z" fill="#7cc23a"/><path d="M5 11h3l2 7h8l2-5H9" fill="none" stroke="#fff" stroke-width="1.6"/><circle cx="11" cy="21" r="1.4" fill="#fff"/><circle cx="17" cy="21" r="1.4" fill="#fff"/></svg></div>
<div class="offer abs" style="left:287px"><div class="offer-photo abs" style="background:linear-gradient(90deg,#8a4a2a,#c98a5a,#7a3e22)" role="img" aria-label="Striped bamboo frame moulding samples"></div><div class="offer-badge abs">Special<br>Offer<br>25%</div><svg class="offer-cart abs" viewBox="0 0 24 26"><path d="M0 8 12 0 24 8V26H0Z" fill="#7cc23a"/><path d="M5 11h3l2 7h8l2-5H9" fill="none" stroke="#fff" stroke-width="1.6"/><circle cx="11" cy="21" r="1.4" fill="#fff"/><circle cx="17" cy="21" r="1.4" fill="#fff"/></svg></div>
<div class="offer abs" style="left:489px"><div class="offer-photo abs" style="background:radial-gradient(#6f7a3a 0 45%,#e6c39a 47%)" role="img" aria-label="Bamboo frame with a beach photo"></div><div class="offer-badge abs">Special<br>Offer<br>25%</div><svg class="offer-cart abs" viewBox="0 0 24 26"><path d="M0 8 12 0 24 8V26H0Z" fill="#7cc23a"/><path d="M5 11h3l2 7h8l2-5H9" fill="none" stroke="#fff" stroke-width="1.6"/><circle cx="11" cy="21" r="1.4" fill="#fff"/><circle cx="17" cy="21" r="1.4" fill="#fff"/></svg></div>
<div class="offer abs" style="left:691px"><div class="offer-photo abs" style="background:radial-gradient(#7a6a5a 0 45%,#1c1c1c 47% 55%,#e6c39a 57%)" role="img" aria-label="Bamboo frame with a barn wedding photo"></div><div class="offer-badge abs">Special<br>Offer<br>25%</div><svg class="offer-cart abs" viewBox="0 0 24 26"><path d="M0 8 12 0 24 8V26H0Z" fill="#7cc23a"/><path d="M5 11h3l2 7h8l2-5H9" fill="none" stroke="#fff" stroke-width="1.6"/><circle cx="11" cy="21" r="1.4" fill="#fff"/><circle cx="17" cy="21" r="1.4" fill="#fff"/></svg></div>

<section class="newsletter abs"></section>
<div class="badge abs" role="img" aria-label="Partner badge"></div>
<div class="parcel abs"><h2 class="abs">Join Our Newsletter!</h2></div>
<div class="email abs">Enter Your Email</div>
<div class="submit abs">Submit!</div>

<div class="grass abs"></div>
<div class="col-head abs" style="left:86px">EasyMount Blog</div>
<div class="col-head abs" style="left:285px">Customer Testimonials</div>
<div class="col-head abs" style="left:489px">Latest Tweets</div>
<div class="col-head abs" style="left:689px">Tag Cloud</div>

<ul class="blog abs">
  <li>Trade Photo Frames in Bulk</li><li>Mount Prices Slashed by upto 40%</li><li>New Moulding - Time to get creative.</li><li>Website Updates</li>
  <li>Trade Photo Frames in Bulk</li><li>Mount Prices Slashed by upto 40%</li><li>New Moulding - Time to get creative.</li><li>Website Updates</li>
</ul>

<div class="quote abs" style="top:946px">Have ordered again from you today<br>and am looking forward to sitting back<br>knowing I don't need to &#8221;<a href="#">Read More / Add Testimonial</a></div>
<div class="quote abs" style="top:1022px">Have ordered again from you today<br>and am looking forward to sitting back<br>knowing I don't need to &#8221;<a href="#">Read More / Add Testimonial</a></div>
<div class="quote abs" style="top:1096px">Have ordered again from you today<br>and am looking forward &#8221;<a href="#">Read More / Add Testimonial</a></div>

<p class="tweets abs" style="top:949px"><b>about 10 hours ago</b> Order today and<br>your #pictureframes will be dispatched<br>by Weds 31st Oct at the latest. Order<br>from <span>http://lnk.ex/4Qm7x</span> Fast</p>
<p class="tweets abs" style="top:1011px"><b>about 10 hours ago</b> Order today and<br>your #pictureframes will be dispatched<br>by Weds 31st Oct at the latest. Order<br>from <span>http://lnk.ex/4Qm7x</span> Fast</p>
<p class="tweets abs" style="top:1081px"><b>about 10 hours ago</b> Order today and<br>your #pictureframes will be dispatched<br>by Weds 31 <span>http://lnk.ex/4Qm7x Fast</span></p>

<p class="tags abs">trade picture frames ready made<br>photo frames cheap photo frames<br>collage frames cheap picture frames<br><span class="big">multi opening mounts</span><br><span class="big">multi aperture frames</span><br><span class="big">canvas floater</span> frames floater<br>frames swept picture frames budget<br>picture framing polcore picture<br>frames canvas frames multi mounts</p>

<footer class="copyright abs">Copyright &copy; 2006-2012 lumaeco Gallery and Framing T/A lumaeco-frames.example | Registered Office: 4 Fernleaf Row, Millbrook, Ashford, AB12 3CD,</footer>
</body>
</html>
```